Cobalt Ridge Goods Co.
Cobalt Ridge Goods Co. business cards - Miscellaneous
Cobalt Ridge Goods Co. business cards
Professional
Trevor Kasmund
President
Denver | Colorado | USA
trev@cobaltridgegoods.example
www.cobaltridgegoods.example
I would like the logo to be on the front of the business card preferably the size of the height of the card on the left side
I would like the logo to be on the back of the business card as well. The logo should take up the entire back of the business card.
quartzfen quartzfen
Kindly do some star rating... it will really help us to make stationary for your like designs.. thanks!
kasmundtk kasmundtk
We are also looking for at stationary options. Please provide any options for letterhead, etc..

```html
<!DOCTYPE html>
<html lang="en">
<head>
<meta charset="utf-8">
<title>Cobalt Ridge Goods Co. — Business Cards</title>
<link rel="stylesheet" href="https://fonts.googleapis.com/css2?family=Open+Sans:wght@400;700;800&display=swap">
<style>
  :root {
    --backdrop: #8c8c8c;
    --card: #ffffff;
    --navy: #23237a;
    --title-blue: #2e3f8f;
    --text-grey: #8a8a8a;
    --web-red: #e0242b;
  }
  html, body {
    margin: 0;
    padding: 0;
    width: 1200px;
    height: 871px;
    overflow: hidden;
    background: var(--backdrop);
    font-family: "Open Sans", Arial, sans-serif;
  }
  .stage {
    position: relative;
    width: 1200px;
    height: 871px;
  }
  .card {
    position: absolute;
    background: var(--card);
    box-shadow: 0 6px 18px rgba(0,0,0,0.35);
    box-sizing: border-box;
  }

  /* Front */
  .card-front {
    left: 60px;
    top: 250px;
    width: 655px;
    height: 374px;
  }
  .front-mark {
    position: absolute;
    left: 42px;
    top: 40px;
    width: 220px;
    height: 294px;
    display: flex;
    flex-direction: column;
    justify-content: center;
    gap: 8px;
  }
  .brand-name {
    margin: 0;
    color: var(--navy);
    font-weight: 800;
    text-transform: uppercase;
  }
  .front-mark .brand-name {
    font-size: 42px;
    line-height: 1.08;
  }
  .brand-square {
    background: var(--navy);
    flex: none;
  }
  .front-mark .brand-square {
    width: 22px;
    height: 22px;
  }
  .holder {
    position: absolute;
    right: 34px;
    top: 34px;
    text-align: right;
  }
  .holder-name {
    margin: 0;
    color: var(--title-blue);
    font-weight: 700;
    font-size: 21px;
  }
  .holder-role {
    margin: 4px 0 0;
    color: var(--text-grey);
    font-size: 14px;
  }
  .contact {
    position: absolute;
    left: 302px;
    top: 178px;
    color: var(--text-grey);
    font-size: 15px;
    line-height: 1.5;
  }
  .contact p { margin: 0; }
  .contact .city { margin-bottom: 14px; }
  .contact .phone { letter-spacing: 1.5px; }
  .contact .web {
    margin-top: 16px;
    color: var(--web-red);
    font-weight: 700;
    font-size: 16px;
  }

  /* Back */
  .card-back {
    left: 790px;
    top: 112px;
    width: 370px;
    height: 648px;
    padding: 0 26px;
    display: flex;
    flex-direction: column;
    justify-content: center;
    gap: 18px;
  }
  .card-back .brand-name {
    font-size: 72px;
    line-height: 1.08;
  }
  .card-back .brand-square {
    width: 44px;
    height: 44px;
  }
</style>
</head>
<body>
<main class="stage">
  <section class="card card-front">
    <div class="front-mark">
      <p class="brand-name">Cobalt<br>Ridge<br>Goods Co.</p>
      <div class="brand-square"></div>
    </div>
    <div class="holder">
      <p class="holder-name">Trevor Kasmund</p>
      <p class="holder-role">President</p>
    </div>
    <div class="contact">
      <p class="city">Denver | Colorado | USA</p>
      <p class="phone">720.555.0148</p>
      <p class="email">trev@cobaltridgegoods.example</p>
      <p class="web">www.cobaltridgegoods.example</p>
    </div>
  </section>

  <section class="card card-back">
    <p class="brand-name">Cobalt<br>Ridge<br>Goods<br>Co.</p>
    <div class="brand-square"></div>
  </section>
</main>
</body>
</html>
```